Window graphics designed like Venetian blinds with message/ graphic poking out

Hi there.
I need someone to create a window graphic that has a changeable picture that I can replace (and get reprinted) depending on whatever offer I'm currently promoting.
visually, I'm after some Venetian blinds graphics that has a secondary picture in the middle. Not sure how, but if it's possible to have the file so that my printer can also change the bands colours, I'd appreciate it.
I have attached a picture that I took of a similar graphic as well as a picture of the windows it'll be on ( 3* 71cm wide *160 in height)
many thanks
Martin

```html
<!DOCTYPE html>
<html lang="en">
<head>
<meta charset="utf-8">
<title>Venetian Blind Window Graphics</title>
<link rel="stylesheet" href="https://fonts.googleapis.com/css2?family=Lato:wght@400;700&display=swap">
<style>
  :root {
    --page: #ffffff;
    --slat: #3e7d9c;
    --slat-shadow: #336c88;
    --slat-edge: #4da3bf;
    --cord: #2b5a55;
    --text-light: #f1f6f7;
    --text-accent: #86e4ec;
    --skin-light: #f6cdb2;
    --skin-dark: #d99a7c;
  }
  html, body {
    margin: 0;
    width: 1200px;
    height: 1200px;
    overflow: hidden;
    background: var(--page);
  }
  .artboard { display: block; width: 1200px; height: 1200px; }
  .slat-base { stop-color: var(--slat); }
  .slat-shade { stop-color: var(--slat-shadow); }
  .slat-edge { stop-color: var(--slat-edge); }
  .blind { fill: url(#slats); }
  .cord { stroke: var(--cord); stroke-width: 4; fill: none; }
  .cord-tassel { fill: var(--cord); }
  .skin-a { stop-color: var(--skin-light); }
  .skin-b { stop-color: var(--skin-dark); }
  .hand-area { fill: url(#skin); }
  .copy {
    font-family: "Lato", sans-serif;
    font-weight: 700;
    font-size: 17px;
    letter-spacing: 4px;
    text-anchor: middle;
    fill: var(--text-light);
  }
  .copy .accent { fill: var(--text-accent); }
  .social-dot { fill: #3b4f8c; }
</style>
</head>
<body>
<svg class="artboard" viewBox="350 -129 1280 1280" xmlns="http://www.w3.org/2000/svg">
  <defs>
    <linearGradient id="slat-fill" x1="0" y1="0" x2="0" y2="1">
      <stop offset="0" class="slat-edge"/>
      <stop offset="0.08" class="slat-shade"/>
      <stop offset="0.25" class="slat-base"/>
      <stop offset="0.92" class="slat-base"/>
      <stop offset="1" class="slat-shade"/>
    </linearGradient>
    <pattern id="slats" patternUnits="userSpaceOnUse" x="0" y="96" width="40" height="35">
      <rect width="40" height="35" fill="url(#slat-fill)"/>
    </pattern>
    <linearGradient id="skin" x1="0" y1="0" x2="1" y2="1">
      <stop offset="0" class="skin-a"/>
      <stop offset="1" class="skin-b"/>
    </linearGradient>
  </defs>

  <!-- Upper blind panels -->
  <rect class="blind" x="398" y="95" width="365" height="453"/>
  <rect class="blind" x="805" y="96" width="367" height="455"/>
  <rect class="blind" x="1219" y="96" width="364" height="451"/>

  <!-- Lower blind panels, pulled open -->
  <polygon class="blind" points="398,578 763,632 763,922 398,922"/>
  <polygon class="blind" points="805,636 990,672 1172,636 1172,927 805,927"/>
  <polygon class="blind" points="1219,632 1583,580 1583,919 1219,919"/>

  <!-- Pull cords -->
  <line class="cord" x1="426" y1="95" x2="426" y2="752"/>
  <line class="cord" x1="443" y1="95" x2="443" y2="692"/>
  <rect class="cord-tassel" x="420" y="745" width="12" height="24" rx="6"/>
  <rect class="cord-tassel" x="437" y="686" width="12" height="24" rx="6"/>

  <!-- Hands parting the slats -->
  <rect class="hand-area" x="1012" y="528" width="92" height="50" rx="22" role="img" aria-label="Hands pulling the upper blind up"/>
  <rect class="hand-area" x="938" y="640" width="106" height="42" rx="20" role="img" aria-label="Hands pushing the lower blind down"/>

  <!-- Left panel: social -->
  <text class="copy" x="584" y="328">FOLLOW US:</text>
  <circle class="social-dot" cx="486" cy="355" r="9"/>
  <text class="copy" x="592" y="361"><tspan class="accent">@kevinmartinfloat</tspan></text>

  <!-- Centre panel: message -->
  <text class="copy" x="994" y="331"><tspan class="accent">SUBMERGE</tspan> INTO PURE</text>
  <text class="copy" x="990" y="365"><tspan class="accent">RELAXATION.</tspan></text>
  <text class="copy" x="990" y="399"><tspan class="accent">FLOAT</tspan> YOUR WAY TO</text>
  <text class="copy" x="990" y="433"><tspan class="accent">REJUVENATION.</tspan></text>

  <!-- Right panel: contact -->
  <text class="copy" x="1400" y="330">CONTACT US:</text>
  <text class="copy" x="1400" y="362">+44(0) 1632 960481</text>
  <text class="copy" x="1400" y="395">tryus@<tspan class="accent">martinfloats</tspan>.me</text>
</svg>
</body>
</html>
```